One of Australia's fastest growing energy maintenance contractors needs a new website

www.brightpane.com.au
Our business has evolved over the past years and now our website is no longer relevant.
We clean solar panels and we vacuum roof gutters.
We clean solar panels on the roofs of residential houses right up to billion dollar solar farms with in excess of 1 million panels. We offer thermal image testing and bird proofing for our residential and commercial clients and thermal drone imaging services for our solar farm clients.
We vacuum clean roof gutters (using a LoftSuk) on the residential house next door right up to enormous private and public schools, colleges, shopping centres, strat complexes and commercial buildings.
When first built our business had more of a domestic residential skew and the website reflected that. While that is still part of our core business we are now bidding on and have secured large government, commercial and infrastructure contracts and our new website needs to reflect our growth and our new business. We need a new site that it optimised for both desktop ad phone viewing as our latest figures showed that 73% of people visiting our site are on mobile phones. We have an extensive amount of data on Vesti Metrics available as well as Promos. Both that would also need integrating with the site along with a few other plugins such as Qarlo Chat Desk, Pallio etc along with SEO key words etc. We are also the winner and finalists over multiple years of the small business of the year awards and we like to proudly and prominently display those on our site.
We are looking for a new site with a modern professional feel / theme
There is a definitive break in our business between the solar Panel cleaning clients and the gutter cleaning clients so we would like a home page that begins with a simple choice:
Solar Panel Cleaning – Gutter Cleaning
With a professional full screen background image (we have hundreds to choose from) and along the bottom a small area with rights reserved etc, phone number etc (at some point in the future we will split these into two businesses but for now it’s what we have).
After that selection is made we would like a repeat of that same scenario but the selection is:
If it’s Solar Panel Cleaning
(new background image)
Government – Infrastructure – Commercial – Residential
If it’s Gutter Cleaning
(new background image)
Government – Strata – Commercial – Residential
After making those choices then onto the relevant pages with background images relevant to each sector and a them that suits (on the residential we would like to keep the link to our vesti ratings) - We will provide copy / text for each relevant page.
Other than that, a menu inclusive of the above and:
Resellers Portal – we will provide a link to this from Qarlo CRM)
Customer portal (we will supply a link to this from our booking system)
We also need a page for our Solar Resellers / Partners page but we will give them a link to this, it won’t be listed on the site.
Request a quote page (Again we will provide information from Qarlo as this will be linked to the CRM)
Standard contact us page inclusive of phone numbers, address and fields supplied from CRM
Sydney – 02 7391 5083
Southern Highlands – 02 4860 3178
Goulburn – 02 4860 3178
Canberra – 02 6172 8354
Wollongong – 02 4239 6017
sales@brightpane.com.au
Head Office - Ferndale Rise NSW 2590
ABN: 48906237115
Responsive Design: Optimized for desktop and mobile (73% mobile visitors).
Fast Loading Speed: Optimized for performance.
Smooth Transition Animations: For service and category selection.
Sticky Contact Bar: Always accessible at the bottom of mobile screens for quick calls.
SEO Optimization: Focused on government tenders, large-scale commercial contracts, and infrastructure projects.
Integrations
Vesti Metrics & Vesti Promos.
Qarlo Chat Desk.
Pallio Beacon.
SEO tools and keyword optimization.
Many many more images available if needed

```html
<!DOCTYPE html>
<html lang="en">
<head>
<meta charset="utf-8">
<title>Brightpane – Solar Cleaning &amp; Vacuum Roof Gutters Cleaning</title>
<link rel="stylesheet" href="https://fonts.googleapis.com/css2?family=Outfit:wght@300;400;500;600;700&display=swap">
<style>
:root{
  --blue:#1b93da;
  --blue-light:#2aa8e8;
  --blue-dark:#0b5ba9;
  --navy:#0a3f7c;
  --navy-deep:#08346a;
  --heading:#0f64b2;
  --text:#3b4350;
  --muted:#6d7480;
  --white:#ffffff;
  --star:#f5a623;
  --line:#e3e8ef;
}
*{box-sizing:border-box;margin:0;padding:0}
html,body{width:1200px;height:3734px;overflow:hidden}
body{font-family:'Outfit',sans-serif;color:var(--text);background:var(--white);position:relative}
.abs{position:absolute}

/* header */
.site-header{position:absolute;left:0;top:0;width:1200px;height:72px;background:var(--white);z-index:5}
.brand{position:absolute;left:100px;top:14px;display:flex;align-items:center;gap:12px}
.brand-mark{width:40px;height:40px;background:var(--blue);border-radius:6px}
.brand-name{font-size:28px;font-weight:500;color:var(--heading)}
.main-nav{position:absolute;top:27px;left:377px;font-size:14px;color:#2e3a4a}
.main-nav a{position:absolute;white-space:nowrap;color:inherit;text-decoration:none}
.btn-header{position:absolute;left:1003px;top:19px;width:145px;height:33px;background:var(--blue-dark);color:#fff;font-size:13px;font-weight:600;display:flex;align-items:center;justify-content:center;gap:4px}

/* hero */
.hero{position:absolute;left:0;top:72px;width:1200px;height:670px;background:linear-gradient(90deg,#5d7d9e 0%,#c6dcee 30%,#e3eef8 50%,#c9dced 70%,#5a6f88 100%)}
.hero-label{position:absolute;left:473px;top:134px;width:286px;height:28px;background:var(--navy);color:#fff;font-size:15px;font-weight:600;letter-spacing:2px;display:flex;align-items:center;justify-content:center;transform:skewX(-18deg)}
.hero-label span{transform:skewX(18deg)}
.hero-title{position:absolute;left:0;top:166px;width:1200px;text-align:center;font-size:46px;font-weight:600;line-height:50px;color:var(--heading)}
.hero-title .light{color:var(--blue-light)}
.hero-sub{position:absolute;left:0;top:277px;width:1200px;text-align:center;font-size:15px;color:#2d3a4c}
.btn-primary{position:absolute;background:var(--blue-dark);color:#fff;font-weight:600;display:flex;align-items:center;justify-content:center;gap:6px}
.hero .btn-primary{left:523px;top:244px;width:190px;height:48px;font-size:16px}

/* service choice cards */
.service-card{position:absolute;top:611px;width:500px;height:248px;color:#fff;text-align:center}
.service-card.solar{left:96px;background:linear-gradient(180deg,#2aa8ea,#1984cc)}
.service-card.gutter{left:604px;background:linear-gradient(180deg,#0d5aa8,#0b4b8f)}
.service-icon{position:absolute;left:202px;top:-48px;width:96px;height:96px;border-radius:50%;border:6px solid #fff;display:flex;align-items:center;justify-content:center}
.solar .service-icon{background:var(--navy)}
.gutter .service-icon{background:var(--blue-light)}
.service-card h2{position:absolute;left:0;top:88px;width:100%;font-size:25px;font-weight:600}
.service-card p{position:absolute;left:100px;top:128px;width:300px;font-size:14px;line-height:19px}
.service-card .chev{position:absolute;left:238px;top:182px}

/* section headings */
.section-title{position:absolute;left:0;width:1200px;text-align:center;font-size:41px;font-weight:600;color:var(--heading)}
.title-dot{position:absolute;width:26px;height:26px;border-radius:4px;background:var(--blue)}

/* photo tiles */
.tile{position:absolute;overflow:hidden}
.tile-label{position:absolute;left:22px;bottom:16px;color:#fff;font-size:25px;font-weight:600}

/* gutter band */
.gutter-band{position:absolute;left:0;top:1543px;width:1200px;height:497px;background:linear-gradient(90deg,#0b5aa8,#1b7fcf 60%,#2aa3e6)}
.gutter-intro{position:absolute;left:0;top:1805px;width:1200px;text-align:center;color:#fff;font-size:18px}
.strata-card{position:absolute;left:340px;top:1878px;width:265px;height:327px;background:linear-gradient(180deg,#123d66,#0a2f58);color:#fff;padding:0 30px}
.strata-card h3{position:absolute;left:30px;top:72px;font-size:24px;font-weight:600}
.strata-card p{position:absolute;left:39px;top:114px;width:200px;font-size:13px;line-height:18px}
.strata-card .learn{position:absolute;left:43px;top:236px;font-size:12px;text-decoration:underline}

/* testimonials */
.review{position:absolute;top:2410px;width:294px;height:262px;background:#fff;border:1px solid var(--line);box-shadow:0 4px 14px rgba(20,60,110,.08);padding:30px 32px}
.review .quote{font-size:40px;font-weight:700;color:var(--blue);line-height:24px;height:30px}
.review p{font-size:12.5px;line-height:20px;color:var(--muted);margin-top:10px}
.review .stars{color:var(--star);font-size:17px;letter-spacing:2px;margin-top:8px}
.review .author{font-size:14px;font-weight:600;color:var(--navy);margin-top:8px}
.arrow-btn{position:absolute;top:2518px;width:48px;height:48px;border-radius:50%;background:#fff;box-shadow:0 3px 10px rgba(0,0,0,.12);display:flex;align-items:center;justify-content:center}

/* footer */
.site-footer{position:absolute;left:0;top:3200px;width:1200px;height:534px;background:linear-gradient(180deg,#0c58a6,#0a4c93)}
.copyright{position:absolute;left:0;top:3669px;width:1200px;height:65px;background:#0a4585;color:#dce8f5;font-size:13px;display:flex;align-items:center;justify-content:center}

/* quote form */
.quote-box{position:absolute;left:136px;top:2801px;width:936px;height:497px;background:linear-gradient(180deg,#2aa6e8,#1b8ed6)}
.quote-title{position:absolute;left:0;top:2845px;width:1200px;text-align:center;font-size:39px;font-weight:600;color:#fff}
.field{position:absolute;background:#fff;height:53px;display:flex;align-items:center;gap:12px;padding-left:18px;font-size:15px;color:#4a5260}
.field.message{align-items:flex-start;padding-top:16px;height:122px}
.quote-box-btn{left:507px;top:3208px;width:209px;height:52px;font-size:16px;background:var(--navy)}

.footer-col h4{font-size:18px;font-weight:600;letter-spacing:1.5px;color:#fff;padding-bottom:10px;border-bottom:1px solid rgba(255,255,255,.45);display:inline-block}
.footer-col ul{list-style:none;margin-top:18px}
.footer-col li{color:#e3eefa;font-size:14px;line-height:23px;display:flex;align-items:center;gap:7px}
.contact-list li{line-height:26px}
.social{display:flex;gap:8px}
.social span{width:29px;height:29px;border-radius:50%;background:#fff}
</style>
</head>
<body>

<header class="site-header">
  <div class="brand"><span class="brand-mark"></span><span class="brand-name">Brightpane</span></div>
  <nav class="main-nav">
    <a style="left:0">Solar Cleaning</a>
    <a style="left:120px">Gutter Cleaning</a>
    <a style="left:250px">Resellers Portal</a>
    <a style="left:381px">Customer portal</a>
    <a style="left:517px">Contact Us</a>
  </nav>
  <a class="btn-header">Request a Quote ›</a>
</header>

<section class="hero" role="img" aria-label="Workers cleaning solar panels and a roof with a pressure hose under a bright sky">
</section>
<div class="hero-label"><span>WELCOME TO BRIGHTPANE</span></div>
<h1 class="hero-title">Solar Cleaning &amp; Vacuum<br><span class="light">Roof Gutters Cleaning</span></h1>
<p class="hero-sub" style="top:277px">We have a detailed knowledge of the cleaning &amp; testing of Solar Panels</p>
<a class="btn-primary" style="left:523px;top:316px;width:190px;height:48px;font-size:16px">GET A QUOTE ›</a>

<div class="service-card solar">
  <div class="service-icon">
    <svg width="46" height="40" viewBox="0 0 46 40" fill="none" stroke="#fff" stroke-width="2"><path d="M6 4h34l4 22H2z"/><path d="M2 15h42M16 4l-2 22M30 4l2 22"/><path d="M23 26v10M14 37h18"/></svg>
  </div>
  <h2>SOLAR PANEL CLEANING</h2>
  <p>Lorem ipsum dolor sit amet consectetur adipiscing elit sed do eiusmod</p>
  <svg class="chev" width="24" height="14" viewBox="0 0 24 14"><path d="M2 2l10 10L22 2" stroke="#fff" stroke-width="3" fill="none"/></svg>
</div>
<div class="service-card gutter" style="top:611px">
  <div class="service-icon">
    <svg width="50" height="34" viewBox="0 0 50 34" fill="none" stroke="#fff" stroke-width="2"><path d="M4 30L16 4h30v26z"/><path d="M22 10v20M29 10v20M36 10v20M43 10v20"/></svg>
  </div>
  <h2 style="top:91px">ROOF GUTTER CLEANING</h2>
  <p style="top:131px">Lorem ipsum dolor sit amet consectetur adipiscing elit sed do eiusmod</p>
  <svg class="chev" style="top:185px" width="24" height="14" viewBox="0 0 24 14"><path d="M2 2l10 10L22 2" stroke="#fff" stroke-width="3" fill="none"/></svg>
</div>

<!-- solar sectors -->
<span class="title-dot" style="left:587px;top:906px"></span>
<h2 class="section-title" style="top:940px">Solar Panel Cleaning</h2>

<div class="tile" style="left:119px;top:1027px;width:471px;height:239px;background:linear-gradient(160deg,#b7c9d6,#6e5a3c 55%,#3f5130)" role="img" aria-label="Solar panels on a government building roof at sunset"><span class="tile-label">| Government</span></div>
<div class="tile" style="left:604px;top:1027px;width:471px;height:239px;background:linear-gradient(180deg,#9cc0dc,#5b87b0 45%,#1d3d6a)" role="img" aria-label="Solar farm with power lines"><span class="tile-label">| Infrastructure</span></div>
<div class="tile" style="left:120px;top:1282px;width:471px;height:239px;background:linear-gradient(180deg,#a9c2d6,#2f5a88 45%,#2b2f36)" role="img" aria-label="Solar carport over parked cars"><span class="tile-label">| Commercial</span></div>
<div class="tile" style="left:607px;top:1282px;width:471px;height:239px;background:linear-gradient(180deg,#7fb6e6,#2c3c58 55%,#3a4150)" role="img" aria-label="Solar panels on a residential house roof"><span class="tile-label">| Residential</span></div>

<!-- gutter sectors -->
<div class="gutter-band" role="img" aria-label="Blue tinted background of gutter cleaning work"></div>
<svg class="abs" style="left:0;top:1543px" width="1200" height="124" viewBox="0 0 1200 124"><path d="M0 0H1200L600 124z" fill="#fff"/></svg>
<span class="title-dot" style="left:587px;top:1708px;background:#fff"></span>
<h2 class="section-title" style="top:1744px;color:#fff">Gutter Cleaning</h2>
<p class="gutter-intro">Lorem ipsum dolor sit amet, consectetur adipiscing elit sed do eiusmod incid</p>

<div class="tile" style="left:75px;top:1895px;width:265px;height:290px;background:linear-gradient(180deg,#8fb8e2,#c9d9e8 40%,#2c3644)" role="img" aria-label="Government office building with a tower"><span class="tile-label">| Government</span></div>
<div class="strata-card" role="group" aria-label="Strata">
  <h3>| Strata</h3>
  <p>Lorem ipsum dolor sit amet, consectetur adipiscing elit, sed do eiusmod tempor incididunt ut labore et dolore magna aliqua. Quis ipsum suspendisse ultrices gravida Risus</p>
  <span class="learn">LEARN MORE ›</span>
</div>
<div class="tile" style="left:605px;top:1895px;width:265px;height:290px;background:linear-gradient(180deg,#c8a43a,#3d4a58 45%,#1f2a38)" role="img" aria-label="Flat commercial roof at sunset"><span class="tile-label">| Commercial</span></div>
<div class="tile" style="left:871px;top:1895px;width:265px;height:290px;background:linear-gradient(180deg,#c9d2dc,#7d8896 50%,#3a4452)" role="img" aria-label="Residential house roof with gutters"><span class="tile-label">| Residential</span></div>

<!-- testimonials -->
<span class="title-dot" style="left:582px;top:2272px"></span>
<h2 class="section-title" style="top:2306px">What People Says</h2>

<div class="arrow-btn" style="left:59px"><svg width="20" height="14" viewBox="0 0 20 14"><path d="M19 7H2M8 1L2 7l6 6" stroke="#1a3a60" stroke-width="2" fill="none"/></svg></div>
<article class="review" style="left:152px"><div class="quote">“</div><p>“Lorem ipsum dolor sit amet, consectetur adipiscing elit, sed do eiusmod tempor incididunt ut labore et dolore magna aliqua. Ut enim ad minim veniam, quis nostrud exercitation ullamco laboris nisi ut aliquip ex ea c</p><div class="stars">★★★★★</div><div class="author">By Author name</div></article>
<article class="review" style="left:458px"><div class="quote">“</div><p>“Lorem ipsum dolor sit amet, consectetur adipiscing elit, sed do eiusmod tempor incididunt ut labore et dolore magna aliqua. Ut enim ad minim veniam, quis nostrud exercitation ullamco laboris nisi ut aliquip ex ea c</p><div class="stars">★★★★★</div><div class="author">By Author name</div></article>
<article class="review" style="left:772px"><div class="quote">“</div><p>“Lorem ipsum dolor sit amet, consectetur adipiscing elit, sed do eiusmod tempor incididunt ut labore et dolore magna aliqua. Ut enim ad minim veniam, quis nostrud exercitation ullamco laboris nisi ut aliquip ex ea c</p><div class="stars">★★★★★</div><div class="author">By Author name</div></article>
<div class="arrow-btn" style="left:1095px"><svg width="20" height="14" viewBox="0 0 20 14"><path d="M1 7h17M12 1l6 6-6 6" stroke="#1a3a60" stroke-width="2" fill="none"/></svg></div>

<!-- footer background + quote form -->
<footer class="site-footer" role="img" aria-label="Dark blue background of solar panels"></footer>
<section class="quote-box" role="img" aria-label="Blue tinted solar panel background"></section>
<h2 class="quote-title">Request a Quote</h2>

<div class="field" style="left:235px;top:2926px;width:368px">
  <svg width="18" height="18" viewBox="0 0 18 18" fill="none" stroke="#8a93a0" stroke-width="1.4"><circle cx="9" cy="6" r="4"/><path d="M2 17c1-4 4-6 7-6s6 2 7 6"/></svg>First Name*</div>
<div class="field" style="left:613px;top:2926px;width:368px">
  <svg width="18" height="18" viewBox="0 0 18 18" fill="none" stroke="#8a93a0" stroke-width="1.4"><circle cx="9" cy="6" r="4"/><path d="M2 17c1-4 4-6 7-6s6 2 7 6"/></svg>Last Name*</div>
<div class="field" style="left:235px;top:2994px;width:368px">
  <svg width="22" height="16" viewBox="0 0 22 16" fill="none" stroke="#8a93a0" stroke-width="1.4"><rect x="1" y="1" width="20" height="14"/><path d="M1 1l10 8 10-8"/></svg>E-mail*</div>
<div class="field" style="left:613px;top:2994px;width:368px">
  <svg width="18" height="18" viewBox="0 0 18 18" fill="none" stroke="#8a93a0" stroke-width="1.4"><path d="M4 1l3 4-2 2c1 3 3 5 6 6l2-2 4 3-2 3C8 17 1 10 1 3z"/></svg>Phone number*</div>
<div class="field message" style="left:235px;top:3060px;width:748px">
  <svg width="22" height="20" viewBox="0 0 22 20" fill="none" stroke="#8a93a0" stroke-width="1.4"><path d="M11 2c5 0 9 3 9 7s-4 7-9 7c-1 0-2 0-3-1l-5 2 1-4C2 12 2 10 2 9c0-4 4-7 9-7z"/></svg>Leave Message</div>
<a class="btn-primary quote-box-btn" style="position:absolute">SEND MESSAGE ›</a>

<!-- footer content -->
<div class="abs" style="left:144px;top:3410px;width:140px;height:70px;display:flex;justify-content:center"><span style="width:62px;height:62px;background:#fff;border-radius:8px"></span></div>
<div class="abs" style="left:94px;top:3494px;width:240px;text-align:center;font-size:33px;font-weight:500;color:#fff">Brightpane</div>
<div class="abs social" style="left:130px;top:3549px" aria-label="Social media links"><span></span><span></span><span></span><span></span><span></span></div>

<div class="abs footer-col" style="left:384px;top:3394px">
  <h4>NAVIGATION</h4>
  <ul><li>Home</li><li>Solar Cleaning</li><li>Gutter Cleaning</li><li>Resellers Portal</li><li>Customer portal</li><li>Contact Us</li></ul>
</div>

<div class="abs footer-col" style="left:585px;top:3394px">
  <h4>CONTACT US</h4>
  <ul class="contact-list">
    <li><svg width="12" height="12" viewBox="0 0 18 18" fill="#fff"><path d="M4 1l3 4-2 2c1 3 3 5 6 6l2-2 4 3-2 3C8 17 1 10 1 3z"/></svg>Sydney – 02 7391 5083</li>
    <li><svg width="12" height="12" viewBox="0 0 18 18" fill="#fff"><path d="M4 1l3 4-2 2c1 3 3 5 6 6l2-2 4 3-2 3C8 17 1 10 1 3z"/></svg>Southern Highlands – 02 4860 3178</li>
    <li><svg width="12" height="12" viewBox="0 0 18 18" fill="#fff"><path d="M4 1l3 4-2 2c1 3 3 5 6 6l2-2 4 3-2 3C8 17 1 10 1 3z"/></svg>Goulburn – 02 4860 3178</li>
    <li><svg width="12" height="12" viewBox="0 0 18 18" fill="#fff"><path d="M4 1l3 4-2 2c1 3 3 5 6 6l2-2 4 3-2 3C8 17 1 10 1 3z"/></svg>Canberra – 02 6172 8354</li>
    <li><svg width="12" height="12" viewBox="0 0 18 18" fill="#fff"><path d="M4 1l3 4-2 2c1 3 3 5 6 6l2-2 4 3-2 3C8 17 1 10 1 3z"/></svg>Wollongong – 02 4239 6017</li>
  </ul>
</div>

<div class="abs footer-col" style="left:882px;top:3397px">
  <h4>GET IN TOUCH</h4>
  <ul>
    <li style="margin-top:6px"><svg width="16" height="12" viewBox="0 0 22 16" fill="none" stroke="#fff" stroke-width="2"><rect x="1" y="1" width="20" height="14"/><path d="M1 1l10 8 10-8"/></svg>sales@brightpane.com.au</li>
  </ul>
  <div style="display:flex;gap:8px;margin-top:20px;color:#e3eefa;font-size:14px;line-height:22px">
    <svg width="14" height="20" viewBox="0 0 14 20" fill="#fff"><path d="M7 0a7 7 0 0 1 7 7c0 5-7 13-7 13S0 12 0 7a7 7 0 0 1 7-7zm0 4a3 3 0 1 0 0 6 3 3 0 0 0 0-6z"/></svg>
    <div>Head Office -<br>Ferndale Rise NSW 2590<br>ABN: 48906237115</div>
  </div>
</div>

<div class="copyright">Copyright © 2025 Brightpane. All Right Reserved</div>

</body>
</html>
```